I want a CD cover for a single release that incorporates my photo. Simple classy and beautiful. I have attached my photo and a clip of the video. The artwork should include my name, Darnell Whitford and the title of the song "Rise Up Together". I also would like to use this for other promos so in designing where you put the title of the song, it can be replaced with another title.
Target Market(s)
Gospel Music Industry

```html
<!DOCTYPE html>
<html lang="en">
<head>
<meta charset="utf-8">
<title>Rise Up Together – Darnell Whitford</title>
<link href="https://fonts.googleapis.com/css2?family=Big+Shoulders+Display:wght@500&family=Lato:wght@700&display=swap" rel="stylesheet">
<style>
  :root {
    --teal-deep: #1f4557;
    --teal-mid: #2c5a6e;
    --teal-light: #336579;
    --title-ink: #e6eaee;
    --name-ink: #ffffff;
    --photo-light: #8a8c8e;
    --photo-dark: #1b1b1c;
  }
  html, body {
    margin: 0;
    padding: 0;
    width: 1200px;
    height: 1200px;
    overflow: hidden;
    background: var(--teal-deep);
  }
  .cover {
    position: relative;
    width: 1200px;
    height: 1200px;
    overflow: hidden;
    background: radial-gradient(ellipse at 50% 50%, var(--teal-light) 0%, var(--teal-mid) 45%, var(--teal-deep) 100%);
  }
  .title-stack {
    position: absolute;
    inset: 0;
  }
  .title-row {
    font-family: "Big Shoulders Display", "Arial Narrow", sans-serif;
    font-weight: 500;
    font-size: 300px;
    fill: none;
    stroke: var(--title-ink);
    stroke-width: 2.2;
  }
  .title-row .solid {
    fill: var(--title-ink);
    stroke: none;
  }
  .artist-photo {
    position: absolute;
    left: 339px;
    top: 248px;
    width: 521px;
    height: 781px;
    background: linear-gradient(180deg, var(--photo-light) 0%, #5b5d5f 35%, #2a2a2b 65%, var(--photo-dark) 100%);
  }
  .artist-name {
    position: absolute;
    inset: 0;
  }
  .artist-name text {
    font-family: "Lato", "Helvetica Neue", sans-serif;
    font-weight: 700;
    font-size: 34px;
    fill: var(--name-ink);
  }
</style>
</head>
<body>
<main class="cover">
  <svg class="title-stack" width="1200" height="1200" viewBox="0 0 1200 1200" aria-label="Rise Up Together, repeated four times">
    <text class="title-row" x="85" y="263" textLength="1033" lengthAdjust="spacingAndGlyphs"><tspan class="solid">R</tspan>ISE UP TOGET<tspan class="solid">H</tspan>ER</text>
    <text class="title-row" x="85" y="484" textLength="1033" lengthAdjust="spacingAndGlyphs">R<tspan class="solid">I</tspan>SE UP TOGETH<tspan class="solid">E</tspan>R</text>
    <text class="title-row" x="85" y="920" textLength="1033" lengthAdjust="spacingAndGlyphs">RI<tspan class="solid">S</tspan>E UP TOGETH<tspan class="solid">E</tspan>R</text>
    <text class="title-row" x="85" y="1136" textLength="1033" lengthAdjust="spacingAndGlyphs">RIS<tspan class="solid">E</tspan> UP TOGETHE<tspan class="solid">R</tspan></text>
  </svg>

  <div class="artist-photo" role="img" aria-label="Portrait photo of the artist in a black vest, turtleneck and cross pendant against a grey studio backdrop"></div>

  <svg class="artist-name" width="1200" height="1200" viewBox="0 0 1200 1200">
    <text x="157" y="612" textLength="893" lengthAdjust="spacing">DARNELL WHITFORD</text>
  </svg>
</main>
</body>
</html>
```